Veterinary TPLO Surgery Flyer Design

Please use this flyer to make a professional-looking 1 page, double-sided client handout regarding TPLO.

You can visit our website at www.brackenfieldpetcare.com & www.northwoodsanimalsurgerygroup.com for additional logo information. The flyer should include all the text from the one provided.

Target Market(s)

Client communication to for referral surgery between sister veterinary clinics

Industry/Entity Type

Veterinary

Requirements
Must have
• The text included
Nice to have
• Nice to have the Cedar Hollow Avenue Animal CLinic & Dr. Pell Mobile vet logos incorporated.

```html
<!DOCTYPE html>
<html lang="en">
<head>
<meta charset="utf-8">
<title>TPLO Surgery Client Handout</title>
<link rel="stylesheet" href="https://fonts.googleapis.com/css2?family=Montserrat:wght@500;600;700&family=Arimo:wght@400;700&display=swap">
<style>
:root{
  --navy:#2d3a7b;
  --green:#4a6b1c;
  --yellow:#ecd95c;
  --ink:#4d4d4d;
  --paper:#ffffff;
  --backdrop:#5f5f5f;
}
*{margin:0;padding:0;box-sizing:border-box}
html,body{width:1200px;height:842px;overflow:hidden;background:var(--backdrop)}
.canvas{position:relative;width:1200px;height:842px}
.page{position:absolute;top:80px;width:480px;height:679px;background:var(--paper);overflow:hidden;font-family:"Arimo",Arial,sans-serif;color:var(--ink)}
.page--front{left:98px}
.page--back{left:618px}
.hero-photo{position:absolute;left:0;top:0;width:480px;height:330px;
  background:linear-gradient(180deg,#6f7d3e 0%,#8c9a55 30%,#b2a66a 55%,#a8a860 75%,#7f9a3e 100%)}
.hero-subject{position:absolute;left:290px;top:110px;width:140px;height:200px;border-radius:45%;
  background:radial-gradient(ellipse at center,#c98a45 0%,#c98a4500 70%)}
.waves{position:absolute;left:0;top:0}
.title{position:absolute;left:22px;top:48px;font-family:"Montserrat",sans-serif;font-weight:700;color:var(--yellow);font-size:29px;line-height:29px}
.byline{position:absolute;left:26px;top:106px;font-family:"Montserrat",sans-serif;font-weight:600;color:#fff;font-size:20px;white-space:nowrap}
.creds{position:absolute;left:97px;top:132px;width:150px;text-align:right;font-family:"Montserrat",sans-serif;font-weight:600;color:#fff;font-size:11px}
.rule{position:absolute;left:26px;top:145px;width:29px;height:1px;background:#fff;opacity:.8}
.subtitle{position:absolute;left:25px;top:149px;color:#fff;font-size:14px;line-height:21px;white-space:nowrap}
.badge{position:absolute;border-radius:50%;background:#fff;display:flex;align-items:center;justify-content:center;gap:4px;
  font-family:"Arimo",sans-serif;font-weight:700;color:var(--navy);text-align:center}
.badge::before{content:"";width:7px;height:7px;border-radius:50%;background:var(--navy)}
.badge--front{left:27px;top:200px;width:116px;height:116px;font-size:11px}
.section-title{position:absolute;font-family:"Montserrat",sans-serif;font-weight:700;color:var(--navy);font-size:11px;letter-spacing:.1px;white-space:nowrap}
.body{position:absolute;font-size:6.8px;line-height:8.7px;color:var(--ink)}
.figure{position:absolute}
.figure--diagram{left:26px;top:457px;width:160px;height:140px;background:linear-gradient(90deg,#c9c9c4,#e2e0d4 45%,#c7c7c3)}
.figure--xray{left:191px;top:456px;width:180px;height:142px;background:linear-gradient(90deg,#111 0%,#3c3c3c 30%,#1a1a1a 55%,#555 80%,#111 100%)}
.footer-links{position:absolute;left:30px;top:629px;color:#fff;font-weight:700;font-size:9.6px;line-height:11.5px}
/* back */
.band{position:absolute;left:30px;height:15px;width:440px}
.band svg{position:absolute;left:0;top:0}
.band-label{position:absolute;left:9px;top:2.5px;font-family:"Montserrat",sans-serif;font-weight:700;color:#fff;font-size:8.4px;line-height:10px;letter-spacing:.1px;white-space:nowrap}
.list{position:absolute;left:30px;width:410px;font-size:6.8px;line-height:8.7px;color:var(--ink)}
.list b{color:var(--navy)}
.list p{margin-bottom:2.6px}
.process b{font-size:7.6px}
.contact{position:absolute;color:#fff}
.contact h3{font-family:"Arimo",sans-serif;font-weight:700;font-size:9.6px;line-height:11.5px}
.contact .addr{font-size:7px;line-height:8.6px;margin-top:9px}
.contact .phone{font-weight:700;font-size:9.6px;margin-top:8px}
.contact .mail{font-size:7px;line-height:8px}
.contact .web{font-size:7px;margin-top:9px}
.badge--back{left:370px;top:578px;width:86px;height:86px;font-size:9px}
</style>
</head>
<body>
<div class="canvas">

  <section class="page page--front">
    <div class="hero-photo" role="img" aria-label="Photo of a golden retriever running across a sunny lawn with trees behind">
      <div class="hero-subject"></div>
    </div>
    <svg class="waves" width="480" height="330" viewBox="0 0 480 330">
      <path d="M0 265 C60 240 140 230 220 250 C300 270 390 320 480 280 L480 330 L0 330Z" fill="var(--navy)"/>
      <path d="M200 272 C290 300 380 310 480 256 L480 270 C390 318 300 312 200 272Z" fill="var(--green)"/>
      <path d="M0 272 C70 262 150 260 230 282 C320 308 400 322 480 292 L480 330 L0 330Z" fill="#fff"/>
    </svg>

    <div class="title">Advanced<br>Orthopedic Care</div>
    <div class="byline">by Dr. Renata Pell,</div>
    <div class="creds">DVM, DACVS-sa</div>
    <div class="rule"></div>
    <div class="subtitle">TPLO Surgery at<br>Cedar Hollow Avenue Animal Clinic</div>

    <div class="badge badge--front">Renata Pell</div>

    <h2 class="section-title" style="left:32px;top:336px">ABOUT DR. RENATA PELL</h2>
    <p class="body" style="left:30px;top:356px;width:412px">Dr. Renata Pell is a board-certified veterinary surgeon (Diplomate of the American College of Veterinary Surgeons) with over 18 years of experience in small animal surgery. A graduate of Great Lakes State University, she completed her surgical residency at Harborview School of Veterinary Medicine. Through her mobile practice, Roving Surgical Care, Dr. Pell now provides advanced surgical procedures—such as TPLO—directly at local clinics.</p>

    <h2 class="section-title" style="left:29px;top:399px">WHAT IS TPLO SURGERY?</h2>
    <p class="body" style="left:30px;top:419px;width:412px">Tibial Plateau Leveling Osteotomy (TPLO) is a surgical procedure that stabilizes the stifle (knee) joint following a cranial cruciate ligament (CCL) rupture—a common orthopedic injury in dogs. The procedure involves altering the angle of the tibial plateau to eliminate abnormal joint motion, restoring stability and improving function.</p>

    <div class="figure figure--diagram" role="img" aria-label="Illustration of a canine stifle joint before and after TPLO, showing the tibial plateau angle change"></div>
    <div class="figure figure--xray" role="img" aria-label="Pre-op and post-op TPLO radiographs with plateau angle measurements"></div>

    <svg class="waves" style="top:595px" width="480" height="84" viewBox="0 0 480 84">
      <path d="M0 12 C60 -2 130 0 200 12 C300 30 400 45 480 0 L480 84 L0 84Z" fill="var(--navy)"/>
      <path d="M140 6 C260 26 380 60 480 2 L480 14 C380 66 260 34 140 6Z" fill="var(--green)"/>
    </svg>
    <div class="footer-links">www.brackenfieldpetcare.com<br>www.northwoodsanimalsurgerygroup.com</div>
  </section>

  <section class="page page--back">
    <div class="band" style="top:49px">
      <svg width="440" height="15" viewBox="0 0 440 15"><path d="M4 0 H268 L281 14 H0 V4 Q0 0 4 0Z" fill="var(--green)"/><rect x="0" y="14" width="405" height="0.8" fill="var(--green)"/></svg>
      <span class="band-label">BENEFITS OF TPLO SURGERY</span>
    </div>
    <div class="list" style="top:73px">
      <p><b>Enhanced Joint Stability:</b> Restores natural biomechanics, reducing pain and improving mobility.</p>
      <p><b>Faster Recovery:</b> Many dogs return to normal activity faster compared to other surgical techniques.</p>
      <p><b>Proven Long-Term Success:</b> TPLO is particularly effective in large and active breeds</p>
    </div>

    <div class="band" style="top:116px">
      <svg width="440" height="15" viewBox="0 0 440 15"><path d="M4 0 H300 L313 14 H0 V4 Q0 0 4 0Z" fill="var(--green)"/><rect x="0" y="14" width="405" height="0.8" fill="var(--green)"/></svg>
      <span class="band-label" style="font-size:7.9px;letter-spacing:0">WHY CHOOSE CEDAR HOLLOW AVENUE ANIMAL CLINIC?</span>
    </div>
    <div class="list" style="top:142px;width:412px">
      <p>Partnering with Dr. Pell, Cedar Hollow Avenue Animal Clinic offers advanced orthopedic surgery on-site—eliminating the need for referrals or travel. This collaboration ensures your pet receives expert surgical care in a familiar, trusted environment.</p>
      <p style="margin-top:8px;width:320px">Our clinic works directly with your primary veterinarian to share medical records, diagnostics, and prescriptions, ensuring seamless and coordinated care for your pet</p>
      <p style="margin-top:8px;width:320px"><b style="color:var(--ink)">Diagnostic Radiographs vs. TPLO Planning Radiographs</b><br>While diagnostic radiographs may confirm a CCL tear, they are not sufficient for surgical planning. TPLO requires three advanced technique radiographic views with precise measurements, which must be performed under sedation to reduce discomfort and allow accurate positioning</p>
    </div>

    <div class="band" style="top:246px">
      <svg width="440" height="15" viewBox="0 0 440 15"><path d="M4 0 H203 L216 14 H0 V4 Q0 0 4 0Z" fill="var(--green)"/><rect x="0" y="14" width="405" height="0.8" fill="var(--green)"/></svg>
      <span class="band-label">EXPECTED PROCESS</span>
    </div>
    <div class="list process" style="top:272px;width:412px">
      <p><b>1. Diagnosis:</b> Your pet is diagnosed with stifle instability (CCL tear) by your veterinarian.</p>
      <p><b>2. Referral:</b> Your veterinarian contacts the surgical coordinator at Cedar Hollow Avenue Animal Clinic.</p>
      <p><b>3. Consultation:</b> The coordinator contacts you to schedule a 1-hour consultation to review the procedure, estimated costs, and available surgery dates.</p>
      <p><b>4. Planning Radiographs:</b> These specialized X-rays are typically taken during the consultation under light sedation.</p>
      <p><b>5. Surgical Review:</b> Dr. Pell reviews the radiographs and your pet’s medical history to confirm candidacy for TPLO.</p>
      <p><b>6. Deposit:</b> A $3,500 deposit secures Dr. Pell’s travel and surgery date. This is refundable if canceled at least 5 days prior to the scheduled procedure.</p>
      <p><b>7. Surgery Day:</b> Your pet is dropped off in the morning and surgery is performed the same day.</p>
      <p><b>8. Discharge:</b> You’ll receive a post-surgery update and your pet will go home that evening.</p>
    </div>

    <div class="band" style="top:394px">
      <svg width="440" height="15" viewBox="0 0 440 15"><path d="M4 0 H203 L216 14 H0 V4 Q0 0 4 0Z" fill="var(--green)"/><rect x="0" y="14" width="405" height="0.8" fill="var(--green)"/></svg>
      <span class="band-label">POST-OPERATIVE CARE &amp; FOLLOW-UP</span>
    </div>
    <div class="list" style="top:420px;width:330px">
      <p style="margin-bottom:6px">Two follow-up appointments will be scheduled:</p>
      <p style="margin-bottom:1px"><b>4 Weeks Post-Op:</b> Evaluate healing, refill medications, and address any questions.</p>
      <p style="margin-bottom:6px"><b>8 Weeks Post-Op:</b> Sedated radiographs will confirm proper healing of the surgical site and tibia.</p>
      <p>Dr. Pell will stay in direct contact with you during your pet’s recovery using her custom mobile app, which allows for secure messaging and provides detailed post-operative instructions</p>
    </div>

    <svg class="waves" style="top:510px" width="480" height="169" viewBox="0 0 480 169">
      <path d="M0 28 C50 10 120 4 200 14 C300 28 400 60 480 14 L480 169 L0 169Z" fill="var(--navy)"/>
      <path d="M130 8 C250 28 380 82 480 4 L480 16 C380 90 250 40 130 8Z" fill="var(--green)"/>
    </svg>
    <div class="contact" style="left:39px;top:566px">
      <h3>CEDAR HOLLOW AVENUE<br>ANIMAL CLINIC</h3>
      <p class="addr">2240 Cedar Hollow Avenue<br>Marlow, MI 48990</p>
      <p class="phone">(555) 214-3307</p>
      <p class="mail">info@brackenfieldpetcare.com</p>
      <p class="web">www.brackenfieldpetcare.com</p>
    </div>
    <div class="contact" style="left:171px;top:590px">
      <h3>ROVING SURGICAL CARE<br>(Dr. Renata Pell)</h3>
      <p class="phone" style="margin-top:10px">(555) 382-6190</p>
      <p class="mail">drpell@rovingsurgicalcare.com</p>
      <p class="web">www.northwoodsanimalsurgerygroup.com</p>
    </div>
    <div class="badge badge--back">Renata Pell</div>
  </section>

</div>
</body>
</html>
```